Business Card Design Project

looking for business cards with new logo

I am looking to keep with the colors of the logo i posted.  Here are some other details to consider.  I would like my website prominently displayed on the business card with the logo.  my website is www.HavenrockTX.com...it should be spelled this way.

My contact information is:

Daniel P Whitcomb III
Broker/Owner
48391 Cordell Ave., Suite 307
Corvale, Texas 78099
Office: 210-555-0147
Email:  Daniel@HavenrockTX.com

Thank you
Daniel Whitcomb

```html
<!DOCTYPE html>
<html lang="en">
<head>
<meta charset="utf-8">
<title>Havenrock Realty – Business Card</title>
<link rel="stylesheet" href="https://fonts.googleapis.com/css2?family=Josefin+Sans:wght@400;600;700&display=swap">
<style>
  :root {
    --paper: #ffffff;
    --navy: #05318f;
    --sky: #58d7f2;
    --ink: #ffffff;
  }
  html, body {
    margin: 0;
    padding: 0;
    width: 1000px;
    height: 1200px;
    overflow: hidden;
    background: var(--paper);
  }
  .card {
    position: relative;
    width: 1000px;
    height: 1200px;
    font-family: "Josefin Sans", sans-serif;
    color: var(--ink);
  }
  .card-shape {
    position: absolute;
    inset: 0;
  }
  .brand-name {
    position: absolute;
    top: 250px;
    left: 0;
    width: 1000px;
    text-align: center;
    font-size: 92px;
    font-weight: 600;
    letter-spacing: 1px;
    margin: 0;
  }
  .address {
    position: absolute;
    top: 456px;
    left: 0;
    width: 1000px;
    text-align: center;
    font-size: 48px;
    line-height: 62px;
    margin: 0;
  }
  .rule {
    position: absolute;
    top: 595px;
    left: 170px;
    width: 660px;
    height: 3px;
    background: var(--ink);
  }
  .contact {
    position: absolute;
    top: 714px;
    left: 0;
    width: 1000px;
    text-align: center;
  }
  .contact-name {
    font-size: 50px;
    font-weight: 600;
    line-height: 52px;
    margin: 0;
  }
  .contact-title {
    font-size: 38px;
    line-height: 42px;
    margin: 0 0 42px;
  }
  .contact-line {
    font-size: 48px;
    line-height: 52px;
    margin: 0;
  }
  .contact-line b { font-weight: 700; }
  .website {
    font-family: "Josefin Sans", sans-serif;
    font-size: 58px;
    font-weight: 700;
    fill: var(--ink);
    letter-spacing: 1px;
  }
</style>
</head>
<body>
<div class="card">
  <svg class="card-shape" width="1000" height="1200" viewBox="0 0 1000 1200">
    <ellipse cx="500" cy="600" rx="565" ry="598" fill="var(--sky)"/>
    <ellipse cx="500" cy="600" rx="543" ry="577" fill="var(--navy)"/>
    <defs>
      <path id="website-arc" d="M 110 1000 A 560 560 0 0 0 890 1000"/>
    </defs>
    <text class="website">
      <textPath href="#website-arc" startOffset="50%" text-anchor="middle">www.HavenrockTX.com</textPath>
    </text>
  </svg>

  <h1 class="brand-name">Havenrock Realty</h1>

  <p class="address">48391 Cordell Ave., Suite 307<br>Corvale, Texas 78099</p>
  <div class="rule"></div>

  <div class="contact">
    <p class="contact-name">Daniel P Whitcomb III</p>
    <p class="contact-title">Owner/Broker</p>
    <p class="contact-line"><b>P</b>:210-555-0147</p>
    <p class="contact-line"><b>E</b>:Daniel@HavenrockTX.com</p>
  </div>
</div>
</body>
</html>
```